Business Card cabinets and cabinets components making company.

the card should be formal and interesting at the same time. The main colors will be black and white.

Font styles to use
Sans Serif

Colors

Designer to choose only greyscale colors for use in the design.

Requirements
Must have
• At least must have the followings:
office phone
cell phone
address
position
name
email
web

```html
<!DOCTYPE html>
<html lang="en">
<head>
<meta charset="utf-8">
<title>Joinwell Business Card</title>
<link href="https://fonts.googleapis.com/css2?family=Roboto:wght@400;500;700;900&display=swap" rel="stylesheet">
<style>
  :root {
    --backdrop: #a9a9a9;
    --ink: #222222;
    --card-dark: #1f1f1f;
    --card-light: #ffffff;
    --paper-text: #ffffff;
    --muted: #333333;
  }
  * { margin: 0; padding: 0; box-sizing: border-box; }
  html, body {
    width: 1200px; height: 900px; overflow: hidden;
    background: var(--backdrop);
    font-family: "Roboto", Arial, sans-serif;
  }
  .stage { position: relative; width: 1200px; height: 900px; }
  .card {
    position: absolute; left: 285px; width: 630px; height: 360px;
    border-radius: 28px; overflow: hidden;
  }
  .card--back { top: 50px; background: var(--card-dark); color: var(--paper-text); }
  .card--front { top: 490px; background: var(--card-light); color: var(--ink); }

  .wordmark {
    font-weight: 900; letter-spacing: -1px; line-height: 1;
    display: flex; align-items: center; gap: 12px;
  }
  .wordmark__square { width: 22px; height: 22px; border: 4px solid currentColor; }
  .wordmark-rule { height: 2px; background: currentColor; }

  .card--back .brand {
    position: absolute; left: 0; right: 0; top: 110px;
    display: flex; flex-direction: column; align-items: center;
  }
  .card--back .wordmark { font-size: 66px; }
  .card--back .wordmark-rule { width: 400px; margin-top: 12px; }
  .card--back .web {
    position: absolute; left: 0; right: 0; top: 270px;
    text-align: center; font-size: 17px; font-weight: 500; letter-spacing: 0.5px;
  }

  .card--front .brand { position: absolute; left: 48px; top: 50px; }
  .card--front .wordmark { font-size: 60px; }
  .card--front .wordmark-rule { width: 390px; margin-top: 12px; }

  .person { position: absolute; left: 62px; top: 176px; }
  .person__name { font-size: 22px; font-weight: 700; letter-spacing: 0.5px; }
  .person__role { font-size: 17px; color: var(--muted); margin-top: 2px; }

  .contacts { position: absolute; left: 62px; top: 240px; list-style: none; }
  .contacts li {
    display: flex; align-items: center; gap: 10px;
    font-size: 17px; line-height: 24px; color: var(--ink);
  }
  .contacts svg { width: 15px; height: 15px; flex: none; }

  .address {
    position: absolute; right: 44px; top: 246px; text-align: right;
    font-size: 16px; line-height: 22px; color: var(--ink); font-style: normal;
  }
</style>
</head>
<body>
<main class="stage">

  <section class="card card--back" aria-label="Card back">
    <div class="brand">
      <div class="wordmark"><span class="wordmark__square" aria-hidden="true"></span>Joinwell</div>
      <div class="wordmark-rule"></div>
    </div>
    <p class="web">www.joinwell-cabinets.com</p>
  </section>

  <section class="card card--front" aria-label="Card front">
    <div class="brand">
      <div class="wordmark"><span class="wordmark__square" aria-hidden="true"></span>Joinwell</div>
      <div class="wordmark-rule"></div>
    </div>

    <div class="person">
      <p class="person__name">DANIEL HART</p>
      <p class="person__role">Managing Director</p>
    </div>

    <ul class="contacts">
      <li>
        <svg viewBox="0 0 16 16" aria-label="Office phone"><path fill="#222" d="M3.6 1.2l2.3 2.6-1.3 1.8c.8 2 2.6 3.8 4.6 4.6l1.8-1.3 2.6 2.3-1.4 2.6C6.5 14 2 9.5 1 3.9z"/></svg>
        044-555 210 347
      </li>
      <li>
        <svg viewBox="0 0 16 16" aria-label="Cell phone"><rect x="4" y="1" width="8" height="14" rx="1.5" fill="none" stroke="#222" stroke-width="1.6"/><circle cx="8" cy="12.4" r="0.9" fill="#222"/></svg>
        044-555 318 692
      </li>
      <li>
        <svg viewBox="0 0 16 16" aria-label="Email"><rect x="1" y="3" width="14" height="10" fill="#222"/><path d="M1.5 3.5L8 9l6.5-5.5" fill="none" stroke="#fff" stroke-width="1.2"/></svg>
        info@joinwell-cabinets.com
      </li>
      <li>
        <svg viewBox="0 0 16 16" aria-label="Website"><circle cx="8" cy="8" r="6.5" fill="#222"/><path d="M1.5 8h13M8 1.5c-2.4 2.8-2.4 10.2 0 13M8 1.5c2.4 2.8 2.4 10.2 0 13" fill="none" stroke="#fff" stroke-width="0.9"/></svg>
        www.joinwell-cabinets.com
      </li>
    </ul>

    <address class="address">
      17 Millbrook Road,<br>20817 Northvale
    </address>
  </section>

</main>
</body>
</html>
```